established boer goat stud and dorper sheep stud need an updated look

I need a design to promote the boer goat stud and dorper sheep stud, so its clear and simple

Details for business card design Tarwelle Boers and Dorper Sheep Stud. I would like silhouette animal head or full body of a boer goat (not a dairy breed goat) and Dorper sheep. Contact: Maree Cosgrove +61 412836507 Donna Petrakis +61 438571946 Mooroopna North Victoria Australia Email: tarwelle5184@farmpost.net

Industry/Entity Type

Agriculture

Contact Information for Business Card

Tarwelle Boers and Dorper Sheep Stud Maree Cosgrove +61 412836507 Donna Petrakis +61 438571946 tarwelle5184@farmpost.net Mooroopna Victoria Australia

Colors
EE7325
F08F49
F5BC92
FAE3D3
FDF4ED

Requirements
Must have
• My Boer Goats and Dorper Sheep images see my photos

```html
<!DOCTYPE html>
<html lang="en">
<head>
<meta charset="utf-8">
<title>Stud Business Cards</title>
<link href="https://fonts.googleapis.com/css2?family=Montserrat:wght@500;700&display=swap" rel="stylesheet">
<style>
  :root {
    --bg: #e4e4e4;
    --card: #ffffff;
    --charcoal: #2f3038;
    --brown: #8b5a2b;
    --olive: #6f8a4a;
  }
  * { margin: 0; padding: 0; box-sizing: border-box; }
  html, body { width: 1200px; height: 900px; overflow: hidden; background: var(--bg); }
  .card {
    position: absolute;
    left: 275px;
    width: 650px;
    height: 371px;
    background: var(--card);
    border-radius: 26px;
    overflow: hidden;
    box-shadow: 0 6px 18px rgba(0,0,0,0.18);
    font-family: "Montserrat", sans-serif;
  }
  .card--sheep { top: 55px; }
  .card--goat { top: 474px; }
  .card__art { position: absolute; inset: 0; width: 100%; height: 100%; }
  .card__text { position: absolute; right: 38px; bottom: 34px; text-align: right; }
  .card__title {
    font-weight: 700;
    font-size: 33px;
    letter-spacing: 1px;
    line-height: 1.1;
  }
  .card__contact {
    margin-top: 12px;
    font-weight: 500;
    font-size: 16px;
    letter-spacing: 0.5px;
  }
  .card--sheep .card__title { color: var(--charcoal); }
  .card--sheep .card__contact { color: var(--brown); }
  .card--goat .card__title { color: var(--brown); }
  .card--goat .card__contact { color: var(--olive); }
</style>
</head>
<body>

<div class="card card--sheep">
  <svg class="card__art" viewBox="0 0 650 371" preserveAspectRatio="none">
    <defs>
      <linearGradient id="sheepPhoto" x1="0" y1="1" x2="1" y2="0">
        <stop offset="0" stop-color="#8a7448"/>
        <stop offset="0.45" stop-color="#c9ad73"/>
        <stop offset="1" stop-color="#ddc796"/>
      </linearGradient>
    </defs>
    <path role="img" aria-label="Photo of Dorper sheep grazing in a dry paddock"
          d="M0 0 H650 V120 C540 190 420 235 300 258 C180 280 70 295 0 345 Z"
          fill="url(#sheepPhoto)"/>
    <path d="M0 352 C70 302 180 287 300 265 C420 242 540 197 650 127"
          fill="none" stroke="#2f3038" stroke-width="9"/>
    <path d="M20 350 C90 305 190 292 310 272 C430 250 550 205 650 140"
          fill="none" stroke="#8b5a2b" stroke-width="3"/>
  </svg>
  <div class="card__text">
    <div class="card__title">DORPER SHEEP STUD</div>
    <div class="card__contact">755 214 3086 &nbsp;|&nbsp; info@fieldmail.com &nbsp;|&nbsp; www.studpaddock.com</div>
  </div>
</div>

<div class="card card--goat">
  <svg class="card__art" viewBox="0 0 650 371" preserveAspectRatio="none">
    <defs>
      <linearGradient id="goatPhoto" x1="0" y1="0" x2="1" y2="0">
        <stop offset="0" stop-color="#7fa04a"/>
        <stop offset="0.45" stop-color="#a9bd72"/>
        <stop offset="0.7" stop-color="#c2b88a"/>
        <stop offset="1" stop-color="#b8ae84"/>
      </linearGradient>
    </defs>
    <path role="img" aria-label="Photo of Boer goats grazing on green and dry grass"
          d="M0 0 H650 V120 C540 190 420 235 300 258 C180 280 70 295 0 345 Z"
          fill="url(#goatPhoto)"/>
    <path d="M0 352 C70 302 180 287 300 265 C420 242 540 197 650 127"
          fill="none" stroke="#8b5a2b" stroke-width="8"/>
    <path d="M20 350 C90 305 190 292 310 272 C430 250 550 205 650 140"
          fill="none" stroke="#6f8a4a" stroke-width="4"/>
  </svg>
  <div class="card__text">
    <div class="card__title">BOER GOAT STUD</div>
    <div class="card__contact">755 214 3086 &nbsp;|&nbsp; info@fieldmail.com &nbsp;|&nbsp; www.studpaddock.com</div>
  </div>
</div>

</body>
</html>
```